Quorvane Consulting

We focus on Data Recovery but we also do Network Security. We recover data from all types of hard drive form factors 3.5", 2.5", 1", 1.8", 5.25", 8" with any kind of interface IDE(PATA), SATA, mSATA, SCSI, SAS and Fibre Channel. All RAID Arrays 0, 1, 2, 3, 4, 5, 10 including nested levels like RAID 0+1, 1+0, 100, 0+3, 50 and 60, flash drives, like tablets, cellphones, usb drives, memory cards(SD, miniSD, Memory Stick(hovaku))

Actually you can gather any information or text from any data recovery site, cause is usually the same info, we would probably change a couple of things from the description so it wont look the same. One thing though, we want to make clear to users not to attempt data recovery themselves and to ship the faulty device to us, maybe we can illustrate this?

the Data Recovery link can have sub menus like "Data Recovery Process - Data Recovery Services - F.A.Q"

the Penetration Testing can have sub menus like "F.A.Q - Pentest Process - Pentest Services"

Here are links from website so you gather information:

-http://www.brelwick-disks.example/

-http://www.tolvenpathrescue.example/

-http://www.nimbrocore.example/

http://fentaloprestore.example/lp/disk-restore.aspx?src=web&ref=ZQPLx4TrmvaKDJ-wuHafk9RB2x
http://www.vqlt.example/
http://www.pembrastoneflow.example/data-recovery/
http://www.ytsarchiverescue.example/

thanks.

Target Market(s)

Any PC user

Industry/Entity Type

Data Recovery

Requirements
Must have
• - Language and geographic navigation
- Home page navigation
- Global navigation
- Breadcrumbs
Nice to have
• - Sliders
-Drop down navigation

```html
<!DOCTYPE html>
<html lang="en">
<head>
<meta charset="utf-8">
<title>Quorvane Consulting – Data Recovery</title>
<link href="https://fonts.googleapis.com/css2?family=Roboto+Condensed:wght@400;700&family=Roboto:wght@400;500;700&display=swap" rel="stylesheet">
<style>
:root{
  --red:#e3161e;
  --red-text:#d3141c;
  --black:#161616;
  --page:#f2f2f2;
  --white:#ffffff;
  --line:#d8d8d8;
  --text:#333333;
}
*{box-sizing:border-box;margin:0;padding:0}
html,body{width:935px;height:1200px;overflow:hidden}
body{position:relative;background:var(--page);font-family:"Roboto",Arial,sans-serif;color:var(--text)}
.abs{position:absolute}

/* top bar */
.topbar{left:0;top:0;width:935px;height:17px;background:var(--red)}
.topbar-tab{left:702px;top:0;width:233px;height:30px;background:var(--red);clip-path:polygon(0 0,100% 0,100% 100%,6px 100%)}
.topbar-msg{left:114px;top:3px;font-size:8.5px;font-weight:500;color:var(--white);white-space:nowrap}
.lang{left:714px;top:2px;width:88px;height:23px;background:var(--white);border:1px solid #ddd;font-size:8px;color:#444;display:flex;align-items:center}
.lang-flag{width:14px;height:9px;margin:0 6px 0 5px;background:#243a7a;position:relative;overflow:hidden}
.lang-flag::before{content:"";position:absolute;left:0;top:3px;width:14px;height:3px;background:#fff}
.lang-flag::after{content:"";position:absolute;left:5.5px;top:0;width:3px;height:9px;background:#c8102e}
.lang-caret{margin-left:auto;width:19px;height:100%;border-left:1px solid #ddd;display:flex;align-items:center;justify-content:center;color:#999;font-size:7px}

/* header */
.brand{left:108px;top:48px;display:flex;align-items:center;gap:7px}
.brand-mark{width:18px;height:18px;background:var(--red)}
.brand-name{font-family:"Roboto Condensed",sans-serif;font-weight:700;font-size:25px;color:var(--black);white-space:nowrap}
.contact{right:131px;top:52px;text-align:right;font-size:9.5px;color:#555;line-height:19px;font-family:"Roboto Condensed",sans-serif;white-space:nowrap}

/* nav */
.nav-shadow{left:10px;top:118px;width:915px;height:10px;background:radial-gradient(ellipse at center,rgba(0,0,0,.12),rgba(0,0,0,0) 70%)}
.nav{left:94px;top:108px;width:748px;height:38px;background:var(--black);display:flex}
.nav a{font-family:"Roboto Condensed",sans-serif;font-weight:700;font-size:11px;color:var(--white);text-decoration:none;display:flex;align-items:center;justify-content:center;border-right:1px solid #2c2c2c;white-space:nowrap}
.nav .is-current{background:var(--red);width:78px}
.nav-search{margin-left:auto;width:212px;background:var(--red);display:flex;align-items:center;justify-content:center}
.search-field{width:188px;height:25px;background:var(--white);display:flex;justify-content:flex-end}
.search-btn{width:22px;border-left:1px solid #ddd;display:flex;align-items:center;justify-content:center}

.breadcrumb{left:94px;top:156px;font-size:9px;color:#555;display:flex;align-items:center;gap:5px}

/* hero */
.hero{left:94px;top:176px;width:748px;height:308px;background:radial-gradient(ellipse at 70% 40%,#d9d9d9 0%,#8f8f8f 45%,#3a3a3a 100%)}
.hero-hint{position:absolute;left:110px;top:60px;width:180px;height:160px;background:radial-gradient(circle,rgba(160,240,40,.55),rgba(160,240,40,0) 70%)}
.hero-tag{position:absolute;font-family:"Roboto Condensed",sans-serif;font-weight:400;font-size:32px;line-height:38px;padding:0 8px;white-space:nowrap;overflow:hidden}
.hero-tag.one{left:410px;top:92px;width:194px;height:38px;background:var(--red);color:var(--black)}
.hero-tag.two{left:410px;top:136px;width:278px;height:38px;background:var(--black);color:var(--red)}
.hero-dots{position:absolute;left:660px;top:284px;display:flex;gap:7px}
.hero-dots span{width:10px;height:10px;border-radius:50%;background:#3a3a3a;box-shadow:inset 0 1px 2px #000}
.hero-dots .on{background:#e8e8e8}

/* features */
.feature{top:502px;height:82px;background:var(--white);border:1px solid #ddd}
.feature-img{position:absolute;left:6px;top:14px;width:60px;height:56px;border-radius:4px}
.feature-title{position:absolute;left:76px;top:8px;font-family:"Roboto Condensed",sans-serif;font-size:15px;color:var(--red-text);white-space:nowrap}
.feature-text{position:absolute;left:76px;top:34px;width:158px;font-size:9px;line-height:12.5px;color:#444;text-align:justify}

.divider{left:20px;width:895px;height:1px;background:linear-gradient(90deg,transparent,#cfcfcf 15%,#cfcfcf 85%,transparent)}
.section-title{font-family:"Roboto Condensed",sans-serif;font-weight:400;font-size:16px;color:#333;white-space:nowrap}
.section-rule{height:1px;background:var(--line)}

/* welcome */
.welcome-photo{left:93px;top:670px;width:209px;height:163px;background:var(--white);border:1px solid #ccc;padding:4px}
.welcome-photo div{width:100%;height:100%;background:linear-gradient(135deg,#4d6f96,#9fb8d2 50%,#6d7f93)}
.welcome-copy{left:309px;top:668px;width:229px;font-size:8.6px;line-height:14px;text-align:justify}
.welcome-copy .lead{color:var(--red-text);margin-bottom:14px;text-align:left}
.welcome-copy p{color:#444}

/* video */
.video{left:554px;top:661px;width:292px;height:182px;background:var(--white);padding:4px}
.video-screen{width:100%;height:100%;border:2px solid #0d1b24;background:radial-gradient(ellipse at 55% 45%,#a9cde0,#5a93b3 60%,#366f91);position:relative}
.video-bar{position:absolute;left:0;bottom:0;width:100%;height:15px;background:#1a2a35;display:flex;align-items:center;gap:3px;padding:0 4px}
.video-bar i{width:7px;height:7px;border-radius:50%;background:#8fb6cc}
.video-track{flex:1;height:2px;background:#5c7686;margin:0 4px;position:relative}
.video-track::before{content:"";position:absolute;left:0;top:0;width:18%;height:2px;background:#cfe2ec}
.video-time{font-size:5px;color:#cfe2ec;white-space:nowrap}

/* services */
.service{top:917px;width:98px;height:97px;background:var(--white);border:1px solid #e0e0e0;display:flex;flex-direction:column;align-items:center}
.service svg{margin-top:16px;height:46px}
.service-label{margin-top:16px;font-family:"Roboto Condensed",sans-serif;font-weight:700;font-size:8.5px;color:var(--red-text);white-space:nowrap}

.partners{left:94px;top:1037px;width:748px;height:90px;background:var(--white);border:1px solid #e2e2e2;display:flex;align-items:center;justify-content:space-around;padding:0 8px}
.partner{font-family:"Roboto",sans-serif;font-weight:700;font-size:20px;color:#555}

.footer{left:0;top:1146px;width:935px;height:54px;background:var(--black)}
.copyright{left:94px;top:1161px;font-size:9px;color:#ddd;white-space:nowrap}
.social{left:698px;top:1152px;display:flex;gap:7px}
.social span{width:25px;height:25px;border-radius:50%;background:#3d3d3d}
</style>
</head>
<body>

<div class="abs topbar"></div>
<div class="abs topbar-tab"></div>
<div class="abs topbar-msg">Got Questions? We've got answers! LIVE CHAT WITH A SPECIALIST NOW!</div>
<div class="abs lang"><span class="lang-flag"></span>ENGLISH<span class="lang-caret">▼</span></div>

<div class="abs brand"><span class="brand-mark"></span><span class="brand-name">Quorvane Consulting</span></div>
<div class="abs contact">CALL US: 000.000.0000<br>OUR INTERNATIONAL NUMBERS</div>

<div class="abs nav-shadow"></div>
<nav class="abs nav">
  <a class="is-current" href="#">HOME</a>
  <a href="#" style="width:154px">DATA RECOVERY PROCESS</a>
  <a href="#" style="width:162px">DATA RECOVERY SERVICES</a>
  <a href="#" style="width:58px">FAQ</a>
  <a href="#" style="width:84px;border-right:0">CONTACT</a>
  <div class="nav-search">
    <div class="search-field"><span class="search-btn">
      <svg width="9" height="9" viewBox="0 0 10 10"><circle cx="4" cy="4" r="3" fill="none" stroke="#3a5ea8" stroke-width="1.4"/><line x1="6.2" y1="6.2" x2="9.3" y2="9.3" stroke="#3a5ea8" stroke-width="1.6"/></svg>
    </span></div>
  </div>
</nav>

<div class="abs breadcrumb">Home
  <svg width="6" height="11" viewBox="0 0 6 11"><path d="M1 1l4 4.5L1 10" fill="none" stroke="#ccc" stroke-width="1.2"/></svg>
</div>

<section class="abs hero">
  <div role="img" aria-label="Photo of an open hard drive with small figures in protective suits working on the platters" style="position:absolute;inset:0"><div class="hero-hint"></div></div>
  <div class="hero-tag one">YOUR 24/7</div>
  <div class="hero-tag two">RECOVERY HEROES</div>
  <div class="hero-dots"><span class="on"></span><span></span><span></span><span></span></div>
</section>

<div class="abs feature" style="left:94px;width:241px">
  <div class="feature-img" role="img" aria-label="Hard drive illustration" style="background:radial-gradient(circle,#d8d8d8,#9a8a6a 70%,transparent 72%)"></div>
  <div class="feature-title">DEVICES SUPPORTED</div>
  <div class="feature-text">ullamco laboris nisi ut aliquip ex ea commodo consequat. Duis aute irure dolor in reprehenderit in voluptate velit</div>
</div>
<div class="abs feature" style="left:346px;width:243px">
  <div class="feature-img" role="img" aria-label="Recycle bin full of files illustration" style="background:linear-gradient(#c9d6e8,#8a8a8a)"></div>
  <div class="feature-title">DATA FILE RECOVERY</div>
  <div class="feature-text">ullamco laboris nisi ut aliquip ex ea commodo consequat. Duis aute irure dolor in reprehenderit in voluptate velit</div>
</div>
<div class="abs feature" style="left:599px;width:243px">
  <div class="feature-img" role="img" aria-label="Server drive stack illustration" style="background:linear-gradient(#e6e6e6,#9d9d9d)"></div>
  <div class="feature-title">RAID RECOVERY</div>
  <div class="feature-text">ullamco laboris nisi ut aliquip ex ea commodo consequat. Duis aute irure dolor in reprehenderit in voluptate velit</div>
</div>

<div class="abs divider" style="top:600px"></div>

<h2 class="abs section-title" style="left:93px;top:618px">WELCOME</h2>
<div class="abs section-rule" style="left:94px;top:649px;width:444px"></div>
<h2 class="abs section-title" style="left:560px;top:618px">HOW IT WORKS</h2>
<div class="abs section-rule" style="left:560px;top:649px;width:282px"></div>

<div class="abs welcome-photo"><div role="img" aria-label="Photo of a technician holding an open hard drive in a lab"></div></div>
<div class="abs welcome-copy">
  <p class="lead">Sed ut perspiciatis unde omnis iste natus error sit voluptatem accusantium doloremque laudantium, totam rem aperiam</p>
  <p>eaque ipsa quae ab illo inventore veritatis et quasi architecto beatae vitae dicta sunt explicabo. Nemo enim ipsam voluptatem quia voluptas sit aspernatur aut odit aut fugit, sed quia consequuntur magni dolores eos qui ratione voluptatem sequi nesciunt. Neque porro quisquam est, qui dolorem ipsum quia dolor sit amet, consectetur, adipisci velit, sed quia non numquam eius modi tempora incidunt ut labore et dolore magnam</p>
</div>

<div class="abs video">
  <div class="video-screen">
    <svg style="position:absolute;left:115px;top:56px" width="54" height="54" viewBox="0 0 54 54"><circle cx="27" cy="27" r="24" fill="rgba(255,255,255,.18)" stroke="rgba(255,255,255,.7)" stroke-width="3"/><path d="M21 16l16 11-16 11z" fill="rgba(255,255,255,.75)"/></svg>
    <div class="video-bar"><i></i><i></i><i></i><span class="video-track"></span><span class="video-time">0:12 / 3:24 HD</span></div>
  </div>
</div>

<div class="abs divider" style="top:862px"></div>
<h2 class="abs section-title" style="left:94px;top:871px">OUR SERVICES</h2>
<div class="abs section-rule" style="left:94px;top:902px;width:748px"></div>

<div class="abs service" style="left:95px">
  <svg viewBox="0 0 46 46" width="46"><circle cx="23" cy="23" r="21" fill="#111"/><ellipse cx="23" cy="23" rx="9" ry="21" fill="none" stroke="#fff" stroke-width="1.5"/><line x1="2" y1="23" x2="44" y2="23" stroke="#fff" stroke-width="1.5"/><line x1="23" y1="2" x2="23" y2="44" stroke="#fff" stroke-width="1.5"/></svg>
  <span class="service-label">INTERNATIONAL</span>
</div>
<div class="abs service" style="left:225px">
  <svg viewBox="0 0 46 46" width="46"><rect x="3" y="18" width="40" height="16" rx="3" fill="#222"/><rect x="9" y="12" width="26" height="8" rx="1" fill="#bbb"/><rect x="5" y="20" width="36" height="3" fill="#555"/></svg>
  <span class="service-label">FLASH DRIVES</span>
</div>
<div class="abs service" style="left:354px">
  <svg viewBox="0 0 46 46" width="46"><rect x="4" y="3" width="38" height="40" rx="3" fill="#222"/><rect x="7" y="7" width="32" height="32" fill="#2e2e2e"/></svg>
  <span class="service-label">TABLETS</span>
</div>
<div class="abs service" style="left:482px">
  <svg viewBox="0 0 46 46" width="46"><rect x="10" y="1" width="26" height="44" rx="4" fill="#111"/><rect x="12" y="5" width="22" height="34" fill="#333"/></svg>
  <span class="service-label">CELLPHONES</span>
</div>
<div class="abs service" style="left:612px">
  <svg viewBox="0 0 46 46" width="46"><rect x="12" y="1" width="22" height="44" rx="3" fill="#1c1c1c"/><rect x="14" y="34" width="18" height="8" fill="#ddd"/><path d="M23 8v10M20 11l3-3 3 3" fill="none" stroke="#fff" stroke-width="1.3"/></svg>
  <span class="service-label">USB DRIVES</span>
</div>
<div class="abs service" style="left:742px">
  <svg viewBox="0 0 46 46" width="46"><rect x="3" y="10" width="40" height="26" rx="2" fill="#3a3a3a"/><rect x="6" y="13" width="34" height="8" fill="#888"/><rect x="6" y="26" width="20" height="7" fill="#666"/></svg>
  <span class="service-label">MEMORY CARDS</span>
</div>

<div class="abs partners">
  <span class="partner">Dravelle</span>
  <span class="partner">Ostrin</span>
  <span class="partner">Pellumo</span>
  <span class="partner">Karvex</span>
  <span class="partner">Tembrix</span>
  <span class="partner">Sunaro</span>
  <span class="partner">Welkast</span>
</div>

<footer class="abs footer"></footer>
<div class="abs copyright">© 2013 Quorvane consulting. All Rights reserved.</div>
<div class="abs social"><span></span><span></span><span></span><span></span></div>

</body>
</html>
```